Flyer
Zielgruppe
Brandl´s Werkhaus Holz+ Design
Schreinerei
- aus alt mach neu! wir möchten alte Küchen in neuem Glanz erscheinen lassen.
Fronten/ Griffe / Scharniere/ Beleuchtung Arbeitsplatten werden nach Wunsch erneuert
- neue Türen- nach Wunsch restauriert oder neu eingebaut
- Möbelbau auf Maß
Zielgruppe sind:
- Hausbesitzer/ Eigenheimbesitzer
-älteres Publikum
Aufgabenstellung
- der Fleyer soll übersichtlich sein- bitte nur Deutsche Sprache verwenden
- gern zweiseitig ( wir möchen jeden Monat etwas neues bewerben)
- die eine Seite hat ein festes Layout wo folgende Infos zu entnehmen sind:
BITTE! diesen text auf den Fleyer platzieren:
Brandl`s Werkhaus Holz & Design
Ihre Schreinerei aus Mannheim:
Wir fertigen oder reparieren Ihre Traummöbel aus Holz:
Schlafzimmer
Küchen / Esszimmer
Büromöbel
Wohnmöbel
TreppeTüren
Kaminverkleidungen
Sonderanfertigungen
Bitte halten sie sich an die Webseite- Farbthema usw.
+ Bitte nehmen Sie die vorher nachher Fotos - der Zusammenhang muss stimmen
- keine langen Texte mit einfügen- kurz klar und auf den Punkt bringen
Telefonnumer : 0621 5918207
WICHITG: Frühjahr - Rabattaktion soll mit drauf 15 % auf Ihre neue Küche gültig bis zum 01.05-2025

```html
<!DOCTYPE html>
<html lang="de">
<head>
<meta charset="utf-8">
<title>Brandl's Werkhaus Flyer</title>
<link href="https://fonts.googleapis.com/css2?family=Outfit:wght@400;500;600;700;800&display=swap" rel="stylesheet">
<style>
  :root {
    --ink: #000;
    --text: #1c1c1c;
    --paper: #fff;
    --mist: #f1f1f1;
    --band: #e4e4e6;
    --backdrop: #a9a9a9;
    --photo-warm: #c9b9a6;
    --photo-dark: #2a2622;
    --photo-kitchen: #3a3a3e;
  }
  * { box-sizing: border-box; margin: 0; padding: 0; }
  html, body { width: 1200px; height: 1117px; overflow: hidden; }
  body { background: var(--backdrop); font-family: "Outfit", sans-serif; color: var(--text); position: relative; }
  .page { position: absolute; top: 184px; width: 532px; height: 750px; background: var(--paper); overflow: hidden; }
  .page--front { left: 60px; }
  .page--back { left: 616px; }
  .abs { position: absolute; }
  .shape { position: absolute; left: 0; top: 0; }

  /* front */
  .hero-photo { left: 0; top: 40px; width: 532px; height: 470px;
    background: linear-gradient(180deg, #eef0f1 0%, #d8d9da 45%, #3a3a3a 75%, #b5b5b5 100%); }
  .brand-name { left: 0; width: 532px; top: 34px; text-align: center; font-size: 26px; font-weight: 700; letter-spacing: 2px; color: var(--ink); }
  .offer-badge { left: 372px; top: 250px; width: 128px; height: 128px; border-radius: 50%; background: var(--ink); color: var(--paper);
    display: flex; flex-direction: column; align-items: center; justify-content: center; text-align: center; }
  .offer-kicker { font-size: 11px; font-weight: 600; letter-spacing: .5px; text-transform: uppercase; }
  .offer-value { font-size: 36px; line-height: 36px; font-weight: 800; }
  .offer-text { font-size: 11px; line-height: 12px; font-weight: 500; }
  .offer-date { margin-top: 3px; font-size: 9.5px; line-height: 11px; font-weight: 400; }
  .thumb-frame { left: 53px; top: 396px; width: 426px; height: 137px; background: var(--paper); }
  .thumb { top: 400px; width: 206px; height: 129px; }
  .thumb--light { left: 57px; background: linear-gradient(160deg, #e6e3de, var(--photo-warm)); }
  .thumb--dark { left: 269px; background: linear-gradient(160deg, #5a4a3c, var(--photo-dark)); }
  .headline { left: 0; width: 532px; top: 541px; text-align: center; font-size: 34px; line-height: 40px; font-weight: 700; color: var(--ink); }
  .subline { left: 0; width: 532px; top: 585px; text-align: center; font-size: 20px; line-height: 21px; font-weight: 600; color: var(--ink); }
  .detail { left: 0; width: 532px; top: 636px; text-align: center; font-size: 13px; line-height: 14px; }
  .front-web { left: 0; width: 532px; top: 708px; text-align: center; font-size: 18px; font-weight: 600; letter-spacing: 4px; color: var(--paper); }

  /* back */
  .back-photo { left: 266px; top: 0; width: 266px; height: 290px;
    background: linear-gradient(120deg, #c7a27a 0%, #c7a27a 20%, var(--photo-kitchen) 40%, #1f2024 100%); }
  .intro-title { left: 46px; top: 32px; width: 210px; font-size: 16px; line-height: 19px; font-weight: 700; color: var(--paper); letter-spacing: .3px; }
  .intro-rule { left: 48px; top: 76px; width: 88px; height: 2px; background: var(--paper); }
  .intro-text { left: 46px; top: 90px; width: 200px; font-size: 12.5px; line-height: 16px; color: var(--paper); }
  .intro-text strong { font-weight: 600; }
  .services { left: 40px; top: 294px; list-style: none; display: grid; grid-template-columns: 96px 142px; grid-template-rows: repeat(4, 26px); grid-auto-flow: column; }
  .services li { display: flex; align-items: center; gap: 6px; font-size: 11.5px; color: var(--ink); white-space: nowrap; }
  .gallery { left: 290px; top: 297px; width: 206px; height: 419px; background: var(--paper); }
  .gallery-item { width: 97px; height: 97px; }
  .g1 { left: 294px; top: 301px; background: linear-gradient(#9aa4aa, #4a3a30); }
  .g2 { left: 395px; top: 301px; background: linear-gradient(#d9d6d0, #8d8b88); }
  .g3 { left: 294px; top: 405px; background: linear-gradient(#3dc4a8, #2a2a2e); }
  .g4 { left: 395px; top: 405px; background: linear-gradient(#3aa88e, #3a3a3c); }
  .g5 { left: 294px; top: 514px; background: linear-gradient(#a86a3a, #6a4a30); }
  .g6 { left: 395px; top: 514px; background: linear-gradient(#e8ddd0, #b07a40); }
  .g7 { left: 294px; top: 615px; background: linear-gradient(#e4e6ea, #7a5a3a); }
  .g8 { left: 395px; top: 615px; background: linear-gradient(#eeeeee, #8a6a4a); }
  .invite { left: 46px; width: 220px; top: 431px; text-align: center; font-size: 16px; line-height: 17px; font-weight: 700; color: var(--ink); }
  .contact-pill { left: 46px; top: 489px; width: 220px; height: 25px; border-radius: 13px; background: var(--ink); color: var(--paper); text-align: center; font-size: 16px; font-weight: 500; line-height: 25px; letter-spacing: .5px; }
  .contact-row { left: 46px; display: flex; align-items: center; gap: 10px; color: var(--ink); font-weight: 700; }
  .contact-row svg { flex: none; }
  .row-phone { top: 527px; font-size: 20px; }
  .row-address { top: 562px; font-size: 14px; line-height: 15px; }
  .row-mail { top: 603px; font-size: 14px; }
  .row-web { top: 632px; font-size: 14px; }
  .back-footer { left: 0; width: 340px; top: 716px; text-align: center; font-size: 11px; font-weight: 600; color: var(--paper); }
</style>
</head>
<body>

<section class="page page--front">
  <div class="abs hero-photo" role="img" aria-label="Foto: Inhaberpaar mit kleinem Hund auf einem hellgrauen Sofa in einem hellen Wohnraum"></div>
  <svg class="shape" width="532" height="750" viewBox="0 0 532 750" aria-hidden="true">
    <path d="M0 0 H532 V50 Q266 130 0 55 Z" fill="var(--paper)"/>
    <path d="M0 52 Q266 130 532 48 L532 56 Q266 140 0 62 Z" fill="var(--ink)"/>
    <path d="M0 510 Q266 440 532 510 V750 H0 Z" fill="var(--paper)"/>
    <path d="M0 662 Q266 720 532 662 V750 H0 Z" fill="var(--band)"/>
    <path d="M0 734 Q266 640 532 734 V750 H0 Z" fill="var(--ink)"/>
  </svg>
  <div class="abs brand-name">BRANDL'S WERKHAUS</div>
  <div class="abs offer-badge">
    <span class="offer-kicker">Frühjahrs-Aktion</span>
    <span class="offer-value">15 %</span>
    <span class="offer-text">auf Ihre<br>neue Küche</span>
    <span class="offer-date">gültig bis 01.05.2025</span>
  </div>
  <div class="abs thumb-frame"></div>
  <div class="abs thumb thumb--light" role="img" aria-label="Foto: helle restaurierte Küche mit Holzfront und Kühlschrank"></div>
  <div class="abs thumb thumb--dark" role="img" aria-label="Foto: dunkle Küche unter Dachschräge mit warmer Lichtleiste"></div>
  <h1 class="abs headline">AUS ALT MACH NEU!</h1>
  <p class="abs subline">wir möchten alte Küchen in neuem Glanz<br>erscheinen lassen.</p>
  <p class="abs detail">Fronten/ Griffe / Scharniere/ Beleuchtung Arbeitsplatten<br>werden nach Wunsch erneuert</p>
  <p class="abs front-web">www.brandls-werkhaus.de</p>
</section>

<section class="page page--back">
  <div class="abs back-photo" role="img" aria-label="Foto: moderne dunkle Küche mit Holzrückwand, Barhockern und Blumenvase"></div>
  <svg class="shape" width="532" height="750" viewBox="0 0 532 750" aria-hidden="true">
    <rect x="0" y="0" width="266" height="300" fill="var(--ink)"/>
    <path d="M0 233 Q266 330 532 233 V408 H0 Z" fill="var(--mist)"/>
    <path d="M0 662 Q266 720 532 662 V750 H0 Z" fill="var(--band)"/>
    <path d="M0 734 Q266 640 532 734 V750 H0 Z" fill="var(--ink)"/>
  </svg>
  <h2 class="abs intro-title">ENTDECKEN<br>SIE BRANDL'S WERKHAUS</h2>
  <div class="abs intro-rule"></div>
  <p class="abs intro-text"><strong>Brandl`s Werkhaus Holz &amp; Design</strong><br>Ihre Schreinerei aus Mannheim.<br><br>Wir fertigen oder reparieren Ihre Traummöbel aus Holz:</p>

  <ul class="abs services">
    <li><svg width="10" height="10" viewBox="0 0 12 12"><circle cx="6" cy="6" r="6" fill="var(--ink)"/><path d="M3.3 6.2 5.2 8 8.8 4.2" stroke="#fff" stroke-width="1.6" fill="none"/></svg>Schlafzimmer</li>
    <li><svg width="10" height="10" viewBox="0 0 12 12"><circle cx="6" cy="6" r="6" fill="var(--ink)"/><path d="M3.3 6.2 5.2 8 8.8 4.2" stroke="#fff" stroke-width="1.6" fill="none"/></svg>Büromöbel</li>
    <li><svg width="10" height="10" viewBox="0 0 12 12"><circle cx="6" cy="6" r="6" fill="var(--ink)"/><path d="M3.3 6.2 5.2 8 8.8 4.2" stroke="#fff" stroke-width="1.6" fill="none"/></svg>Wohnmöbel</li>
    <li><svg width="10" height="10" viewBox="0 0 12 12"><circle cx="6" cy="6" r="6" fill="var(--ink)"/><path d="M3.3 6.2 5.2 8 8.8 4.2" stroke="#fff" stroke-width="1.6" fill="none"/></svg>Treppen</li>
    <li><svg width="10" height="10" viewBox="0 0 12 12"><circle cx="6" cy="6" r="6" fill="var(--ink)"/><path d="M3.3 6.2 5.2 8 8.8 4.2" stroke="#fff" stroke-width="1.6" fill="none"/></svg>Küchen / Esszimmer</li>
    <li><svg width="10" height="10" viewBox="0 0 12 12"><circle cx="6" cy="6" r="6" fill="var(--ink)"/><path d="M3.3 6.2 5.2 8 8.8 4.2" stroke="#fff" stroke-width="1.6" fill="none"/></svg>Türen</li>
    <li><svg width="10" height="10" viewBox="0 0 12 12"><circle cx="6" cy="6" r="6" fill="var(--ink)"/><path d="M3.3 6.2 5.2 8 8.8 4.2" stroke="#fff" stroke-width="1.6" fill="none"/></svg>Kaminverkleidungen</li>
    <li><svg width="10" height="10" viewBox="0 0 12 12"><circle cx="6" cy="6" r="6" fill="var(--ink)"/><path d="M3.3 6.2 5.2 8 8.8 4.2" stroke="#fff" stroke-width="1.6" fill="none"/></svg>Sonderanfertigungen</li>
  </ul>

  <div class="abs gallery"></div>
  <div class="abs gallery-item g1" role="img" aria-label="Foto: Küche mit Theke, nachher"></div>
  <div class="abs gallery-item g2" role="img" aria-label="Foto: Küche mit Edelstahl-Kühlschrank, vorher"></div>
  <div class="abs gallery-item g3" role="img" aria-label="Foto: Küche mit türkiser Beleuchtung, nachher"></div>
  <div class="abs gallery-item g4" role="img" aria-label="Foto: Küchenzeile mit Einbaugeräten, nachher"></div>
  <div class="abs gallery-item g5" role="img" aria-label="Foto: alte Holzküche, vorher"></div>
  <div class="abs gallery-item g6" role="img" aria-label="Foto: Holzküche mit Hängeschränken, vorher"></div>
  <div class="abs gallery-item g7" role="img" aria-label="Foto: erneuerte weiße Küche mit Holzarbeitsplatte, nachher"></div>
  <div class="abs gallery-item g8" role="img" aria-label="Foto: erneuerte weiße Küchenecke, nachher"></div>

  <p class="abs invite">Lassen Sie uns wunderbare<br>Möbel designen!</p>
  <div class="abs contact-pill">KONTAKT</div>

  <div class="abs contact-row row-phone">
    <svg width="18" height="18" viewBox="0 0 18 18"><circle cx="9" cy="9" r="9" fill="var(--ink)"/><path d="M6 4.5c.6 0 1.5 1.8 1.5 2.3S6.8 7.5 6.8 8c.4 1.3 1.9 2.8 3.2 3.2.5 0 .8-.7 1.2-.7s2.3.9 2.3 1.5-1 1.8-1.9 1.5C8.4 12.8 5.2 9.6 4.5 6.4 4.2 5.5 5.4 4.5 6 4.5Z" fill="#fff"/></svg>
    +49 621 5918207
  </div>
  <div class="abs contact-row row-address">
    <svg width="18" height="18" viewBox="0 0 18 18"><circle cx="9" cy="9" r="9" fill="var(--ink)"/><path d="M9 4a3.3 3.3 0 0 0-3.3 3.3C5.7 9.8 9 13.5 9 13.5s3.3-3.7 3.3-6.2A3.3 3.3 0 0 0 9 4Z" fill="#fff"/><circle cx="9" cy="7.3" r="1.2" fill="var(--ink)"/></svg>
    <span>Lindenhofer Straße 12 68163<br>Mannheim</span>
  </div>
  <div class="abs contact-row row-mail">
    <svg width="18" height="18" viewBox="0 0 18 18"><circle cx="9" cy="9" r="9" fill="var(--ink)"/><rect x="4.5" y="6" width="9" height="6.2" fill="none" stroke="#fff" stroke-width="1"/><path d="M4.5 6 9 9.6 13.5 6" fill="none" stroke="#fff" stroke-width="1"/></svg>
    info@brandls-werkhaus.de
  </div>
  <div class="abs contact-row row-web">
    <svg width="18" height="18" viewBox="0 0 18 18"><circle cx="9" cy="9" r="9" fill="var(--ink)"/><circle cx="9" cy="9" r="4.6" fill="none" stroke="#fff" stroke-width="1"/><ellipse cx="9" cy="9" rx="2" ry="4.6" fill="none" stroke="#fff" stroke-width="1"/><path d="M4.4 9h9.2" stroke="#fff" stroke-width="1"/></svg>
    www.brandls-werkhaus.de
  </div>

  <p class="abs back-footer">Brandl´s Werkhaus Holz+ Design</p>
</section>

</body>
</html>
```